Business Card for Lawyer

I'm looking for a business card for my new law firm, based in Ontario, Canada. I would prefer single sided. I am partial (but not limited) to white and blue color wise and like things understated. Also, if you can work in the red KT rating symbol from Penrowe-Calloway, that would be a plus.

Target Market(s)

Old people - so it should be easy to read.

Industry/Entity Type

Business

Contact Information for Business Card

See the specs in the word document below. Also, see the design for my website. The card should have a similar look to the site.

Requirements
Must have
• Everything listed in the business card specs. I don't mind having the address set off at the bottom of the card on its own line.
Should not have
• 1) Any sort of design that could also be used by a tattoo parlour or a tarot card reader, mystic etc.
• 2) There should not be any photographs of me (or anyone else).

```html
<!DOCTYPE html>
<html lang="en">
<head>
<meta charset="utf-8">
<title>Daniel's Law Firm – Business Card</title>
<link rel="stylesheet" href="https://fonts.googleapis.com/css2?family=Arimo:wght@400;700&display=swap">
<style>
  :root {
    --brand-teal: #0a5570;
    --ink: #1a1a1a;
    --paper: #ffffff;
    --page: #ffffff;
  }
  html, body {
    margin: 0;
    padding: 0;
    width: 1200px;
    height: 722px;
    overflow: hidden;
    background: var(--page);
  }
  .card {
    position: relative;
    width: 1200px;
    height: 722px;
    background: var(--paper);
    font-family: "Arimo", Arial, sans-serif;
    color: var(--ink);
    overflow: hidden;
  }
  .card-shapes {
    position: absolute;
    inset: 0;
  }
  .text {
    position: absolute;
    margin: 0;
    line-height: 1;
    white-space: nowrap;
    font-weight: 400;
  }
  .tagline {
    left: 620px;
    top: 26px;
    font-size: 37px;
    color: var(--paper);
  }
  .rating-mark {
    position: absolute;
    left: 18px;
    top: 168px;
    display: flex;
    align-items: center;
    gap: 12px;
  }
  .rating-dot {
    width: 40px;
    height: 40px;
    border-radius: 50%;
    background: var(--brand-teal);
    flex: none;
  }
  .rating-name {
    font-size: 40px;
    line-height: 1;
    font-weight: 400;
    color: var(--ink);
  }
  .firm-name { left: 207px; top: 110px; font-size: 48px; }
  .lawyer-name { left: 207px; top: 186px; font-size: 50px; }
  .lawyer-title { left: 207px; top: 236px; font-size: 37px; }

  .contact-line {
    position: absolute;
    margin: 0;
    left: 206px;
    display: flex;
    align-items: center;
    gap: 8px;
    font-size: 28px;
    line-height: 28px;
    white-space: nowrap;
  }
  .contact-line svg {
    width: 26px;
    height: 22px;
    fill: var(--ink);
    flex: none;
  }
  .address { top: 366px; }
  .phone { top: 463px; }
  .fax { top: 496px; }
  .website { top: 536px; }
  .email { top: 570px; }
</style>
</head>
<body>
<div class="card">
  <svg class="card-shapes" width="1200" height="722" viewBox="0 0 1200 722" aria-hidden="true">
    <path class="top-band" d="M0 0 H1200 V72 Q600 48 0 108 Z" fill="var(--brand-teal)"/>
    <path class="bottom-band" d="M0 600 Q600 680 1200 600 V722 H0 Z" fill="var(--brand-teal)"/>
    <rect class="divider" x="201" y="319" width="943" height="4" fill="var(--ink)"/>
    <rect class="divider" x="201" y="436" width="943" height="4" fill="var(--ink)"/>
  </svg>

  <p class="text tagline">Getting the results that matter</p>

  <div class="rating-mark"><span class="rating-dot"></span><span class="rating-name">KT</span></div>

  <p class="text firm-name">Daniel’s Law Firm</p>
  <p class="text lawyer-name">Daniel R. Ashcombe</p>
  <p class="text lawyer-title">Lawyer B.A &amp; J.D.</p>

  <p class="contact-line address">
    <svg viewBox="0 0 24 20" aria-hidden="true"><path d="M12 1 L1 11 H4 V19 H10 V13 H14 V19 H20 V11 H23 Z"/></svg>
    <span>48 Larkspur Avenue West , Ground Floor , Dunmore , ON K7P 2R4</span>
  </p>

  <p class="contact-line phone">
    <svg viewBox="0 0 24 20" aria-hidden="true"><path d="M2 6 Q12 -1 22 6 L20 9 L16 7 V5 H8 V7 L4 9 Z"/><path d="M6 10 H18 L20 17 H4 Z"/></svg>
    <span>613-555-xxxx</span>
  </p>
  <p class="contact-line fax">
    <svg viewBox="0 0 24 20" aria-hidden="true"><path d="M6 1 H16 L18 3 V8 H6 Z"/><path d="M2 9 H22 V19 H2 Z M5 12 V14 H19 V12 Z" fill-rule="evenodd"/></svg>
    <span>613.555.xxxx</span>
  </p>
  <p class="contact-line website">
    <svg viewBox="0 0 24 20" aria-hidden="true"><path d="M12 1 A9 9 0 1 0 12.01 1 Z M12 3 A7 7 0 1 1 11.99 3 Z M11 3 H13 V17 H11 Z M5 9 H19 V11 H5 Z" fill-rule="evenodd"/></svg>
    <span>www.danielsfirm.ca</span>
  </p>
  <p class="contact-line email">
    <svg viewBox="0 0 24 20" aria-hidden="true"><path d="M1 4 H23 V18 H1 Z M3 6 L12 12 L21 6 V16 H3 Z" fill-rule="evenodd"/></svg>
    <span>xxxx@danielsfirm.ca</span>
  </p>
</div>
</body>
</html>
```